Layout for location based cityguide with social features

I am building Location Based Social network which is basically a cityguide.
So people would see clearly on map location of places and for each place they can read and write reviews and perhaps add pictures.

Current working version can be browsed in
http://beta.townroam.example/maps/english/United%20States/New%20York/10182

To see innerpages
login: plorv / plorv7

Mainly I need:
-first page, with improved category selection bar.

- Rating / review page for business
- settings page for user
+ general infopage for TOS etc.

Please submit also subpages. Users "home" page and company review page. Review page is the most important one after first page.
Example of review page: http://beta.townroam.example/rating/index/7912

Remember that you need to submit 4 designs in this competition.

Target Market(s)

Tourists or information seekers from the city they are browsing.

Shoppers seeking specific brands from city shops, which are open and can serve them with their desired language (i.e. they are tourists in foreign city)

Industry/Entity Type

Building

Requirements
Must have
• I need four pages in this design contest:
1) First page
-First page must display cityname and categories which are selected to be viewed.
-Language selection, possibility to choose another country/city and search.
-category selection
2) Company information page
-needs: opening hours
-which language they can server customers
-short company presentation
-keyword
-brands which are represented
3) Users home page when he logs in
-link to edit own information
-link to follow people / companies
-list of places added / comments leaved
4) general page for TOS etc.

simplicity is a great plus. I like current layout a lot, mainly because only few colours are used and main focus is in map. All functions needed are in one place and rating was placed in bottom of screen so top5 can be increased if needed.

Logo that fits layout and something I could use in prints etc.

When users first comes to page he will instantly get the wow factor + idea of website.

Call to action style functionality.
Nice to have
• I like the current layout where browsing is done from right and rest of the space is reserved for map.

Information that user has logged in.
Top ratings for selected categories

Typical elements of social networks, sharing and feedback etc.
Should not have
• I have tried layouts where there are lots of stuff in everyside of the map.

Earlier examples, don't make site look like this:
http://1.townroam.example
http://2.townroam.example

Map will get lost in the layout, and this is not what I want.

```html
<!DOCTYPE html>
<html lang="en">
<head>
<meta charset="utf-8">
<title>TownRoam – User Home</title>
<link rel="stylesheet" href="https://fonts.googleapis.com/css2?family=Ubuntu:wght@400;500;700&family=Arimo:wght@400;700&display=swap">
<style>
:root{
  --header-top:#2e2e2e;
  --header-bottom:#5a5a5a;
  --green:#8cb80f;
  --green-dark:#6f9608;
  --green-text:#7aa800;
  --blue:#1a7fd0;
  --blue-dark:#0d63ad;
  --link-blue:#1065b0;
  --heading-blue:#1a5c8c;
  --ink:#1e1e1e;
  --panel:#ffffff;
  --map-tone:#eef0ea;
}
*{box-sizing:border-box;margin:0;padding:0}
html,body{width:1200px;height:884px;overflow:hidden;background:#fff}
body{font-family:Arimo,Arial,sans-serif;color:var(--ink)}
.stage{position:absolute;left:0;top:0;width:1300px;height:958px;transform:scale(.9231);transform-origin:0 0}
.abs{position:absolute}

/* header */
.site-header{left:0;top:0;width:1300px;height:108px;background:linear-gradient(var(--header-top),var(--header-bottom))}
.brand{left:12px;top:4px;color:#fff;font-family:Ubuntu,sans-serif;font-weight:700;font-size:34px;white-space:nowrap}
.tagline{left:12px;top:57px;color:#fff;font-family:Ubuntu,sans-serif;font-size:13px;line-height:19px;font-style:italic;white-space:nowrap}
.brand-art{left:212px;top:24px;width:102px;height:78px;border-radius:6px;background:linear-gradient(135deg,#7fc7d8,#3f8fa8)}
.top-links{right:18px;top:6px;display:flex;align-items:center;gap:10px;color:#fff;font-size:13px}
.flag{width:18px;height:18px;border-radius:50%;background:#3a6ab8;border:2px solid #ddd}
.flag.alt{background:#d9b82a}
.main-nav{right:15px;top:76px;display:flex;font-size:13px;font-weight:700;color:#fff;white-space:nowrap}
.main-nav a{padding:1px 21px;border-left:1px solid #777;color:#fff;text-decoration:none;line-height:18px;white-space:nowrap}
.main-nav a:first-child{border:0;color:var(--green)}
.main-nav a:last-child{padding-right:0}

/* map area */
.map{left:0;top:108px;width:1300px;height:712px;background:radial-gradient(circle at 40% 40%,#f4f5f1,var(--map-tone))}
.map-types{left:1097px;top:114px;display:flex;border:2px solid #222;font-size:12px;background:#fff}
.map-types span{width:66px;text-align:center;border-left:1px solid #222;line-height:15px}
.map-types span:first-child{border:0;font-weight:700}

/* profile */
.profile{left:10px;top:151px;width:997px;height:172px;background:linear-gradient(#fff 70%,#ececec);box-shadow:0 1px 3px rgba(0,0,0,.15)}
.avatar{left:24px;top:162px;width:167px;height:155px;background:linear-gradient(#e8e8e8,#bdbdbd);border:1px solid #ccc}
.profile-info{left:213px;top:172px;font-size:14px;line-height:20px;color:#222}
.profile-info strong{font-family:Ubuntu,sans-serif;font-size:16px;display:block;margin-bottom:2px}
.tab{top:286px;width:111px;height:37px;border-radius:0 14px 0 0;color:#fff;font-family:Ubuntu,sans-serif;font-weight:500;font-size:14px;text-align:center;line-height:40px}
.tab.action{left:308px;background:linear-gradient(var(--blue),var(--blue-dark))}
.tab.review{left:439px;background:linear-gradient(var(--green),var(--green-dark))}
.tab.photos{left:571px;background:linear-gradient(var(--green),var(--green-dark))}

/* ad */
.promo{left:18px;top:363px;width:178px;height:517px;background:linear-gradient(#3a5ad8,#6ea8c8);border:1px solid #ddd}

/* actions */
.actions{left:224px;top:374px;width:520px}
.actions h2{font-family:Ubuntu,sans-serif;font-weight:700;font-size:20px;letter-spacing:.5px;margin-bottom:16px}
.action-item{border-bottom:1px dashed #bbb;height:71px;margin-bottom:0}
.action-item + .action-item{padding-top:16px;height:87px}
.action-item p{font-size:14px;letter-spacing:.6px;white-space:nowrap}
.action-item .hl{color:var(--green-text)}
.action-item time{display:block;color:var(--link-blue);font-size:11px;margin-top:11px}

/* side lists */
.box{left:787px;width:220px;background:var(--panel);border:1px solid #e2e2e2}
.box h3{font-family:Ubuntu,sans-serif;font-weight:500;font-size:18px;color:var(--heading-blue);padding:14px 0 12px 23px}
.box h3.fav{color:#1f7ab8}
.box ul{list-style:none;padding:0 6px 8px 6px}
.box li{display:flex;align-items:center;gap:10px;height:30px;font-size:12px;color:#333;border-bottom:1px dotted #ccc;padding-left:3px;letter-spacing:.3px;white-space:nowrap}
.box li.on{background:var(--green);color:#fff;border:0;width:200px}
.dot{width:12px;height:12px;border-radius:50%;background:#111;flex:none;position:relative}
.on .dot{background:#fff}
.dot::after{content:"";position:absolute;left:3px;top:3px;border-left:6px solid #fff;border-top:3px solid transparent;border-bottom:3px solid transparent}
.on .dot::after{border-left-color:var(--green)}

/* sidebar */
.sidebar{left:1029px;top:152px;width:271px;height:568px;background:#ececec}
.sb-head{left:1029px;top:152px;width:271px;height:52px;background:linear-gradient(var(--green),var(--green-dark));color:#fff;font-family:Ubuntu,sans-serif;padding:2px 10px}
.sb-head b{font-size:21px;display:block}
.sb-head small{font-size:13px;font-weight:700}
.city-search{left:1041px;top:223px;width:248px;height:46px;border-radius:10px;background:linear-gradient(#fafafa,#d8d8d8);border:1px solid #ccc;font-size:12px;font-style:italic;color:#444;padding:15px 12px}
.go-btn{position:absolute;right:8px;top:9px;width:29px;height:27px;border-radius:5px;background:linear-gradient(#3b8ad8,#155aa0)}
.sb-label{left:1039px;top:285px;font-family:Ubuntu,sans-serif;font-size:14px;font-weight:700;color:#555}
.pill{left:1045px;width:228px;height:26px;border-radius:13px;background:#fff;border:1px solid #ccc;font-size:12px;font-style:italic;padding:5px 10px;color:#333;white-space:nowrap}
.pill i{position:absolute;right:9px;top:6px;width:15px;height:13px;border-radius:3px;background:#2a73c2}
.popular{left:1037px;top:391px;font-size:13px;font-weight:700;color:var(--green-text)}
.cities{left:1043px;top:416px;display:grid;grid-template-columns:88px 90px 80px;row-gap:3px;font-size:11px;color:#333;letter-spacing:.3px}
.cities span::before{content:"▸ ";font-size:9px}
.addr-bar{left:1029px;top:551px;width:227px;height:30px;background:var(--green);color:#fff;font-family:Ubuntu,sans-serif;font-weight:700;font-size:14px;display:flex;align-items:center;gap:10px;padding-left:14px}
.addr-link{left:1043px;width:203px;height:32px;border-bottom:1px dotted #bbb;font-family:Ubuntu,sans-serif;font-weight:700;font-size:14px;color:#444;display:flex;align-items:center;gap:10px}
.big-dot{width:17px;height:17px;border-radius:50%;background:#222;position:relative;flex:none}
.addr-bar .big-dot{background:#fff}
.big-dot::after{content:"";position:absolute;left:5px;top:4px;border-left:8px solid #fff;border-top:4.5px solid transparent;border-bottom:4.5px solid transparent}
.addr-bar .big-dot::after{border-left-color:var(--green)}
.connect{left:1065px;top:683px;width:193px;height:23px;background:#3b5a98;color:#fff;font-size:14px;font-weight:700;display:flex;align-items:center;gap:8px;padding-left:8px;white-space:nowrap}
.connect i{width:14px;height:14px;background:#fff;border-radius:2px}
</style>
</head>
<body>
<div class="stage">
  <div class="abs map" role="img" aria-label="Street map of the browsed city"></div>

  <header class="abs site-header"></header>
  <div class="abs brand">TownRoam</div>
  <div class="abs tagline">Social townguide<br>share your city secrets with others</div>
  <div class="abs brand-art" role="img" aria-label="Folded map with location pins"></div>
  <div class="abs top-links"><span>Logout</span><span class="flag" role="img" aria-label="English"></span><span class="flag alt" role="img" aria-label="Swedish"></span><span class="flag" role="img" aria-label="Finnish"></span></div>
  <nav class="abs main-nav"><a>About TownRoam</a><a>The Team</a><a>Press Information</a><a>Advertising</a><a>Term Of Service</a><a>Contact Information</a></nav>

  <div class="abs map-types"><span>Map</span><span>Satellite</span><span>Hybrid</span></div>

  <section class="abs profile"></section>
  <div class="abs avatar" role="img" aria-label="Default profile picture placeholder"></div>
  <div class="abs profile-info"><strong>Testi</strong>Phone:(201)555-0148<br>Email:<br>Website: www.birchwoodtrattoria.example</div>
  <div class="abs tab action">ACTION</div>
  <div class="abs tab review">REVIEW</div>
  <div class="abs tab photos">PHOTO'S</div>

  <div class="abs promo" role="img" aria-label="Travel advertisement banner"></div>

  <section class="abs actions">
    <h2>ACTIONS</h2>
    <div class="action-item" style="height:56px"><p>Testi <span class="hl">Reviewed Restaurant</span> Birchwood Trattoria Nice Experience...</p><time>Nov 30,-0001</time></div>
    <div class="action-item" style="height:85px"><p>Testi <span class="hl">Reviewed Restaurant</span> Birchwood Trattoria Nice Experience...</p><time>Nov 30,-0001</time></div>
    <div class="action-item" style="height:80px"><p>Testi <span class="hl">Reviewed Restaurant</span> Birchwood Trattoria Nice Experience...</p><time>Nov 30,-0001</time></div>
    <div class="action-item" style="height:79px"><p>Testi <span class="hl">Reviewed Restaurant</span> Birchwood Trattoria Nice Experience...</p><time>Nov 30,-0001</time></div>
    <div class="action-item" style="height:89px"><p>Testi <span class="hl">Reviewed Restaurant</span> Birchwood Trattoria Nice Experience...</p><time>Nov 30,-0001</time></div>
    <div class="action-item" style="border:0"><p>Testi <span class="hl">Reviewed Restaurant</span> Birchwood Trattoria Nice Experience...</p><time>Nov 30,-0001</time></div>
  </section>

  <section class="abs box" style="top:345px;height:158px">
    <h3>Edit Profile</h3>
    <ul><li class="on"><span class="dot"></span>Edit Profile</li><li><span class="dot"></span>Change Password</li><li><span class="dot"></span>Change Password</li></ul>
  </section>
  <section class="abs box" style="top:535px;height:158px">
    <h3>Wish List</h3>
    <ul><li class="on" style="width:208px"><span class="dot"></span>Birchwood Trattoria Restaurant</li><li><span class="dot"></span>Birchwood Trattoria</li><li><span class="dot"></span>Birchwood Trattoria</li></ul>
  </section>
  <section class="abs box" style="top:725px;height:158px">
    <h3 class="fav">Favorites</h3>
    <ul><li class="on" style="width:208px"><span class="dot"></span>Birchwood Trattoria Restaurant</li><li><span class="dot"></span>Change Password</li><li><span class="dot"></span>Change Password</li></ul>
  </section>

  <aside class="abs sidebar"></aside>
  <div class="abs sb-head"><b>Currently Browsing</b><small>Newyork City</small></div>
  <div class="abs city-search">-----Select your City----------<span class="go-btn"></span></div>
  <div class="abs sb-label">▸ &nbsp;Change City</div>
  <div class="abs pill" style="top:315px">-----Search City By Name---------<i></i></div>
  <div class="abs pill" style="top:352px">-----Search-----------<i></i></div>
  <div class="abs popular">Popular cities in Finland</div>
  <div class="abs cities"><span>Helsinki</span><span>Vantaa</span><span>Vantaa</span><span>Tampere</span><span>Espoo</span><span>Espoo</span><span>Turku</span><span>Kuopio</span><span>Kuopio</span><span>Oulu</span><span>Pori</span><span>Pori</span></div>
  <div class="abs pill" style="top:501px;left:1041px;font-style:normal">--Choose other covered cities----<i></i></div>
  <div class="abs addr-bar"><span class="big-dot"></span>Go to Address</div>
  <div class="abs addr-link" style="top:584px"><span class="big-dot"></span>Your Location</div>
  <div class="abs addr-link" style="top:616px"><span class="big-dot"></span>Add a Missing Venue</div>
  <div class="abs connect"><i></i>Connect with Friendnet</div>
</div>
</body>
</html>
```